Chiropractic Condition Certificates

Hi,
I'd like have these certificates changed into jpegs with more modern colors and graphics. They need to be eye-catching with good looking images so they will work on Facebook. They need to be suitable to attach in a Facebook post. The current layout might not work for FB post. They may need to be more square then rectangular. Right now they are set up three to a page because In the past they were printed out and handed to patients. I don't need the new ones three to a page. I see these as being used as a jpeg photo in a FB post. Please remove the lines that say "*A $79.00 Value" and the line "MERIDIAN SPINE WELLNESS AND RECOVERY CENTER. 218 HALVERTON AVE. DANBURY, CT 06492 203-555-0187", as they need to be suitable for use by many different chiropractors and not just one.

```html
<!DOCTYPE html>
<html lang="en">
<head>
<meta charset="utf-8">
<title>Chiropractic Condition Certificates</title>
<link rel="stylesheet" href="https://fonts.googleapis.com/css2?family=Didact+Gothic&family=Roboto+Condensed:wght@400;700&display=swap">
<style>
  :root {
    --purple: #7a2f82;
    --purple-dark: #5e1f66;
    --purple-light: #9b4aa3;
    --teal: #1f8793;
    --teal-dark: #156a75;
    --teal-light: #2fa3ad;
    --stone-top: #f1ede9;
    --stone-bottom: #c9c0ba;
    --sand-top: #fbf3cf;
    --sand-bottom: #e6cd88;
    --ink: #2c2a2a;
    --white: #ffffff;
  }
  * { box-sizing: border-box; margin: 0; padding: 0; }
  html, body { width: 1198px; height: 1200px; overflow: hidden; background: var(--white); }
  body { position: relative; font-family: "Roboto Condensed", "Arial Narrow", sans-serif; color: var(--ink); }

  .card {
    position: absolute;
    width: 584px;
    height: 584px;
    border: 1px solid #b9b2ab;
    display: flex;
    flex-direction: column;
    padding: 0 22px 10px;
    overflow: hidden;
  }
  .card--shoulder { --accent: var(--purple); --accent-dark: var(--purple-dark); --accent-light: var(--purple-light);
    background: radial-gradient(ellipse at 50% 35%, var(--stone-top) 0%, #e2dcd7 55%, var(--stone-bottom) 100%); }
  .card--focus { --accent: var(--teal); --accent-dark: var(--teal-dark); --accent-light: var(--teal-light);
    background: radial-gradient(ellipse at 50% 35%, var(--sand-top) 0%, #f3e2a9 55%, var(--sand-bottom) 100%); }

  .pos-tl { left: 10px; top: 0; width: 574px; }
  .pos-tr { left: 614px; top: 0; }
  .pos-bl { left: 10px; top: 616px; width: 574px; }
  .pos-br { left: 614px; top: 616px; }

  .band {
    position: absolute; left: 0; right: 0; top: 56px; height: 84px;
    background: linear-gradient(90deg, var(--accent-dark), var(--accent) 40%, var(--accent-light));
  }
  .photo {
    position: absolute; left: 14px; top: 28px; width: 148px; height: 150px;
    border: 5px solid var(--white);
    box-shadow: 0 3px 8px rgba(0,0,0,.45);
  }
  .photo--shoulder { background: radial-gradient(circle at 45% 30%, #f04a2a 0, #c01a3a 8%, #2a48c8 22%, #0c1d78 70%, #07114a 100%); }
  .photo--focus { background: linear-gradient(160deg, #e9e4d2 0%, #8fb8a0 35%, #2e6a52 60%, #c89a6a 80%, #3b4f78 100%); }

  .headline {
    position: absolute; left: 180px; top: 18px; right: 8px;
    font-family: "Didact Gothic", "Century Gothic", sans-serif;
    line-height: 38px;
  }
  .headline__lead { color: var(--accent); font-size: 33px; display: block; text-transform: uppercase; }
  .headline__lead small, .headline__band small { font-size: 24px; }
  .headline__band { color: var(--white); font-size: 32px; display: block; text-transform: uppercase; }

  .intro {
    position: absolute; left: 182px; right: 22px; top: 152px;
    font-weight: 700; font-size: 15px; line-height: 18px; text-align: justify;
  }

  .body { margin-top: 198px; display: flex; flex-direction: column; gap: 11px; flex: 1; }
  .card--focus .body { margin-top: 204px; }
  .body p { font-size: 14.6px; line-height: 18.5px; text-align: justify; }
  .body--large p { font-size: 17px; line-height: 22.5px; }
  .body--large { gap: 14px; }

  .pass-on { color: var(--accent); font-weight: 700; font-size: 15.5px; margin-top: 2px; }

  .voucher {
    background: var(--accent); padding: 5px; margin-top: 2px;
  }
  .voucher__inner {
    border: 2px solid var(--white); color: var(--white);
    font-weight: 700; font-size: 15.5px; line-height: 19px;
    text-align: center; text-transform: uppercase; padding: 9px 8px;
  }
  .fine-print { font-size: 11px !important; line-height: 13px !important; margin-top: -4px; }

  .share {
    margin-top: auto; margin-bottom: 12px;
    background: var(--accent); padding: 5px;
    box-shadow: 0 2px 5px rgba(0,0,0,.3);
  }
  .share__inner {
    border: 2px solid var(--white); color: var(--white);
    font-weight: 700; font-size: 23px; line-height: 31px;
    text-align: center; padding: 6px 8px;
  }
</style>
</head>
<body>

<section class="card card--shoulder pos-tl">
  <div class="band"></div>
  <div class="photo photo--shoulder" role="img" aria-label="X-ray style illustration of a skeleton with glowing pain points at the shoulder and elbow"></div>
  <h1 class="headline">
    <span class="headline__lead">Help Someone <small>who has</small></span>
    <span class="headline__band">Elbow or Shoulder</span>
    <span class="headline__band">Pain <small>today!</small></span>
  </h1>
  <p class="intro">You may be suffering from shoulder pain needlessly.</p>
  <div class="body">
    <p>Pain in your shoulder can be caused by an injury or inflammation to the joint, muscle, bursa or tendon. For example, “tennis elbow” is the term used to describe inflammation of an elbow tendon. Elbow and shoulder pain can also be cause by misaligned vertebrae in your neck that can pinch the nerve that goes to your arm. Chiropractic care can be successful in relieving and correcting these painful and disabling conditions.</p>
    <p>Our mission in Chiropractic is to help people who are tired of just covering up their pain by taking drugs. We can’t reach everyone personally to tell them that Chiropractic may be the answer to their problem.</p>
    <p>Let’s both offer a helping hand. Refer those you know who could benefit from our care and we will offer our honest and sincere assistance.</p>
    <p class="pass-on">Give this certificate to someone who we can help together through Chiropractic.</p>
    <div class="voucher"><div class="voucher__inner">This gift certificate is valid for 2 weeks and entitles the bearer to a consultation &amp; examination at no charge.</div></div>
    <p class="fine-print">The recipient of this Gift Certificate will have NO charge for the first visit services described above. Should treatment be deemed necessary, the usual fees will be explained in advance. This certificate is not valid for Medicare, Worker’s Comp or Personal Injury cases.</p>
  </div>
</section>

<section class="card card--shoulder pos-tr">
  <div class="band"></div>
  <div class="photo photo--shoulder" role="img" aria-label="X-ray style illustration of a skeleton with glowing pain points at the shoulder and elbow"></div>
  <h2 class="headline">
    <span class="headline__lead">Help Someone <small>who has</small></span>
    <span class="headline__band">Elbow or Shoulder</span>
    <span class="headline__band">Pain <small>today!</small></span>
  </h2>
  <p class="intro">You may be suffering from shoulder pain needlessly.</p>
  <div class="body body--large">
    <p>Pain in your shoulder can be caused by an injury or inflammation to the joint, muscle, bursa or tendon. For example, “tennis elbow” is the term used to describe inflammation of an elbow tendon. Elbow and shoulder pain can also be cause by misaligned vertebrae in your neck that can pinch the nerve that goes to your arm. Chiropractic care can be successful in relieving and correcting these painful and disabling conditions.</p>
    <p>Our mission in Chiropractic is to help people who are tired of just covering up their pain by taking drugs. We can’t reach everyone personally to tell them that Chiropractic may be the answer to their problem.</p>
    <p>Let’s both offer a helping hand. Refer those you know who could benefit from our care and we will offer our honest and sincere assistance.</p>
    <div class="share"><div class="share__inner">Share this messge with someone<br>who we can help together with Chiropractic.</div></div>
  </div>
</section>

<section class="card card--focus pos-bl">
  <div class="band"></div>
  <div class="photo photo--focus" role="img" aria-label="Photo of a bored boy resting his head on his hand at a school desk while a teacher writes on a green chalkboard"></div>
  <h2 class="headline">
    <span class="headline__lead">Help a Child <small>with</small></span>
    <span class="headline__band">Attention Deficit</span>
    <span class="headline__band">Disorder <small>today!</small></span>
  </h2>
  <p class="intro">If your child has been diagnosed with attention deficit disorder, Chiropractic may be able to help.</p>
  <div class="body">
    <p>Interference caused by pressure upon the spinal nerves can send confusing signals across the nervous system. This can result in a shortened attention span and, at times, hyperactivity. A thorough Chiropractic examination can reveal the cause of the problem. The natural approach of Chiropractic and proper nutrition can be very successful in correcting this condition.</p>
    <p>Our mission in Chiropractic is to help people who are tired of just covering up their pain by taking drugs. We can’t reach everyone personally to tell them that Chiropractic may be the answer to their problem.</p>
    <p>Let’s both offer a helping hand. Refer those you know who could benefit from our care and we will offer our honest and sincere assistance.</p>
    <p class="pass-on">Give this certificate to someone who we can help together through Chiropractic.</p>
    <div class="voucher"><div class="voucher__inner">This gift certificate is valid for 2 weeks and entitles the bearer to a consultation &amp; examination at no charge.</div></div>
    <p class="fine-print">The recipient of this Gift Certificate will have NO charge for the first visit services described above. Should treatment be deemed necessary, the usual fees will be explained in advance. This certificate is not valid with Worker’s Comp and Personal Injury cases which often cover 100% of services.</p>
  </div>
</section>

<section class="card card--focus pos-br">
  <div class="band"></div>
  <div class="photo photo--focus" role="img" aria-label="Photo of a bored boy resting his head on his hand at a school desk while a teacher writes on a green chalkboard"></div>
  <h2 class="headline">
    <span class="headline__lead">Help a Child <small>with</small></span>
    <span class="headline__band">Attention Deficit</span>
    <span class="headline__band">Disorder <small>today!</small></span>
  </h2>
  <p class="intro">If your child has been diagnosed with attention deficit disorder, Chiropractic may be able to help.</p>
  <div class="body body--large">
    <p>Interference caused by pressure upon the spinal nerves can send confusing signals across the nervous system. This can result in a shortened attention span and, at times, hyperactivity. A thorough Chiropractic examination can reveal the cause of the problem. The natural approach of Chiropractic and proper nutrition can be very successful in correcting this condition.</p>
    <p>Our mission in Chiropractic is to help people who are tired of just covering up their pain by taking drugs. We can’t reach everyone personally to tell them that Chiropractic may be the answer to their problem.</p>
    <p>Let’s both offer a helping hand. Refer those you know who could benefit from our care and we will offer our honest and sincere assistance.</p>
    <div class="share"><div class="share__inner">Share this messge with someone<br>who we can help together with Chiropractic.</div></div>
  </div>
</section>

</body>
</html>
```